Clean professional design needed for landscape property business

We need a logo for a new lawncare, landscaping , property maintenance business called Fernway Grove.
Our services include lawn mowing, garden maintenance, clean ups and some property maintenance.
We want a double sided business card that is clean and very professional using the colour scheme from our logo which is provided.
the business card should have impact as we will use these to drop into people's letterboxes as a marketing drop.
Initially we want to see what you come up with so there is a very wide scope here to work with.

Project Deadline Extended
Reason: we feel our original deadline was too short. we have extended to give more time for quality submissions.

Target Market(s)

High end property owners who don't wish to do there own gardneing or property maintenance

Industry/Entity Type

Business

Contact Information for Business Card

Name
Postion/ Title
Phone number
mobile
web address
physical address

services offered

Font styles to use
Sans Serif

Requirements
Must have
• curved edges preferrred
Nice to have
• We like the idea of the logo being embossed or etched into the card so it looks like it is below the surface of the card
Should not have
• No stock images or characters.

```html
<!DOCTYPE html>
<html lang="en">
<head>
<meta charset="utf-8">
<title>Fernway Grove – Business Card</title>
<link href="https://fonts.googleapis.com/css2?family=Open+Sans:wght@400;600;700&family=Roboto+Condensed:wght@400&display=swap" rel="stylesheet">
<style>
  :root {
    --canvas: #e9e6e1;
    --card-dark: #2b2b2d;
    --card-light: #f7f7f6;
    --leaf-green: #5fb233;
    --ink-dark: #3a3a3c;
    --ink-mid: #555558;
    --shadow: rgba(0, 0, 0, 0.18);
  }
  * { box-sizing: border-box; margin: 0; padding: 0; }
  html, body {
    width: 1200px;
    height: 1130px;
    overflow: hidden;
    background: var(--canvas);
    font-family: "Open Sans", Arial, sans-serif;
  }
  .canvas {
    position: relative;
    width: 1200px;
    height: 1130px;
  }
  .card {
    position: absolute;
    width: 700px;
    height: 400px;
    border-radius: 18px;
    overflow: hidden;
    box-shadow: 0 10px 30px var(--shadow);
  }

  /* Back side */
  .card-back {
    left: 60px;
    top: 90px;
    background: var(--card-dark);
  }
  .card-back .brand {
    position: absolute;
    left: 0;
    right: 0;
    top: 130px;
    display: flex;
    justify-content: center;
    align-items: center;
    gap: 18px;
  }
  .brand-name {
    font-family: "Open Sans", Arial, sans-serif;
    font-weight: 700;
    color: var(--leaf-green);
    letter-spacing: -1px;
  }
  .card-back .brand-name { font-size: 62px; }
  .brand-mark {
    background: var(--leaf-green);
    border-radius: 50%;
  }
  .card-back .brand-mark { width: 36px; height: 36px; }
  .services {
    position: absolute;
    left: 0;
    right: 0;
    top: 262px;
    text-align: center;
    font-family: "Roboto Condensed", Arial, sans-serif;
    font-size: 21px;
    color: var(--leaf-green);
  }
  .services .divider { margin: 0 8px; }

  /* Front side */
  .card-front {
    left: 440px;
    top: 620px;
    background: var(--card-light);
  }
  .feature-shape {
    position: absolute;
    left: -90px;
    top: 60px;
    width: 320px;
    height: 320px;
    border-radius: 50%;
    background: var(--leaf-green);
  }
  .card-front .brand {
    position: absolute;
    right: 44px;
    top: 44px;
    display: flex;
    align-items: center;
    gap: 10px;
  }
  .card-front .brand-name { font-size: 34px; letter-spacing: -0.5px; }
  .card-front .brand-mark { width: 18px; height: 18px; }
  .person {
    position: absolute;
    left: 300px;
    top: 160px;
  }
  .person-name {
    font-size: 30px;
    color: var(--ink-mid);
    font-weight: 400;
  }
  .person-name strong { font-weight: 700; color: var(--ink-dark); }
  .person-title {
    font-size: 18px;
    color: var(--leaf-green);
  }
  .rule {
    position: absolute;
    left: 300px;
    right: 44px;
    top: 228px;
    height: 2px;
    background: var(--leaf-green);
  }
  .contact-list {
    position: absolute;
    top: 248px;
    list-style: none;
    font-size: 17px;
    color: var(--ink-dark);
  }
  .contact-list li {
    display: flex;
    align-items: center;
    gap: 10px;
    height: 30px;
  }
  .contact-list svg { width: 16px; height: 16px; fill: var(--leaf-green); flex: none; }
  .contact-primary { left: 300px; }
  .contact-online { left: 480px; }
</style>
</head>
<body>
<main class="canvas">

  <section class="card card-back" aria-label="Business card back">
    <div class="brand">
      <span class="brand-name">Fernway Grove</span>
      <span class="brand-mark"></span>
    </div>
    <p class="services">
      lawn mowing<span class="divider">|</span>Garden maintenance<span class="divider">|</span>Clean ups<span class="divider">|</span>Property maintenance
    </p>
  </section>

  <section class="card card-front" aria-label="Business card front">
    <div class="feature-shape" role="img" aria-label="Large green brand symbol decoration"></div>
    <div class="brand">
      <span class="brand-name">Fernway Grove</span>
      <span class="brand-mark"></span>
    </div>
    <div class="person">
      <h1 class="person-name">Your <strong>Name</strong></h1>
      <p class="person-title">JobTitle</p>
    </div>
    <div class="rule"></div>
    <ul class="contact-list contact-primary">
      <li>
        <svg viewBox="0 0 16 16" aria-hidden="true"><path d="M3 1h3l1 4-2 1a9 9 0 0 0 5 5l1-2 4 1v3a2 2 0 0 1-2 2A13 13 0 0 1 1 3a2 2 0 0 1 2-2z"/></svg>
        0000 0000 00
      </li>
      <li>
        <svg viewBox="0 0 16 16" aria-hidden="true"><path d="M4 0h8a1 1 0 0 1 1 1v14a1 1 0 0 1-1 1H4a1 1 0 0 1-1-1V1a1 1 0 0 1 1-1zm1 2v10h6V2z"/></svg>
        0000 0000 00
      </li>
      <li>
        <svg viewBox="0 0 16 16" aria-hidden="true"><path d="M8 0a5.5 5.5 0 0 1 5.5 5.5C13.5 10 8 16 8 16S2.5 10 2.5 5.5A5.5 5.5 0 0 1 8 0zm0 3.5a2 2 0 1 0 0 4 2 2 0 0 0 0-4z"/></svg>
        your address
      </li>
    </ul>
    <ul class="contact-list contact-online">
      <li>
        <svg viewBox="0 0 16 16" aria-hidden="true"><path d="M1 3h14v10H1zm1 1v1l6 4 6-4V4z"/></svg>
        youremail@xyz.com
      </li>
      <li>
        <svg viewBox="0 0 16 16" aria-hidden="true"><path d="M8 0a8 8 0 1 1 0 16A8 8 0 0 1 8 0zm0 1.5C7 2.5 6 4.5 6 7.3h4C10 4.5 9 2.5 8 1.5zM1.6 7.3h3C4.7 5 5.3 3.2 6.2 1.8a6.5 6.5 0 0 0-4.6 5.5zm12.8 0a6.5 6.5 0 0 0-4.6-5.5c.9 1.4 1.5 3.2 1.6 5.5zM1.6 8.7a6.5 6.5 0 0 0 4.6 5.5c-.9-1.4-1.5-3.2-1.6-5.5zm4.4 0c0 2.8 1 4.8 2 5.8 1-1 2-3 2-5.8zm5.4 0c-.1 2.3-.7 4.1-1.6 5.5a6.5 6.5 0 0 0 4.6-5.5z"/></svg>
        yourwebsite.com
      </li>
    </ul>
  </section>

</main>
</body>
</html>
```